Retractable Banner Design for Retail Shopping Event

I need a design for a 33” by 86” retractable banner. It should have my logo at the top (the largest element of the design) and the banner should also include my website and Instagram handle:
www.verikamode.com
@verikamode
I have included product pictures in the brief that can be used. I also included different versions of my logo file, including AI. I need the file to be ready to upload to my printer.
My store is an upscale women’s boutique. I am also attaching designs I have selected in the past to give an idea of my aesthetic.

```html
<!DOCTYPE html>
<html lang="en">
<head>
<meta charset="utf-8">
<title>Verika Mode – Retractable Banner</title>
<link href="https://fonts.googleapis.com/css2?family=Abril+Fatface&family=Playfair+Display:wght@700&family=Quicksand:wght@500&display=swap" rel="stylesheet">
<style>
  :root {
    --page-bg: #d6d6d6;
    --header-pink: #f2d5d7;
    --body-blush: #f7eaeb;
    --accent-rose: #e58c8c;
    --ink: #5a5a5a;
    --circle-face: #f9eff0;
  }
  html, body {
    margin: 0;
    width: 1200px;
    height: 1200px;
    overflow: hidden;
    background: var(--page-bg);
  }
  .banner {
    position: absolute;
    left: 370px;
    top: 60px;
    width: 460px;
    height: 1080px;
    background: var(--body-blush);
    overflow: hidden;
  }
  .banner__header {
    position: absolute;
    left: 0;
    top: 0;
    width: 460px;
    height: 300px;
  }
  .brand {
    position: absolute;
    left: 0;
    top: 110px;
    width: 460px;
    text-align: center;
    color: var(--ink);
    font-family: "Abril Fatface", serif;
    font-weight: 400;
  }
  .brand__name {
    font-size: 58px;
    letter-spacing: 2px;
    line-height: 1;
  }
  .brand__sub {
    margin-top: 22px;
    font-size: 17px;
    letter-spacing: 4px;
    line-height: 1;
  }
  .tagline {
    position: absolute;
    left: 0;
    top: 346px;
    width: 460px;
    text-align: center;
    font-family: "Playfair Display", serif;
    font-weight: 700;
    font-size: 28px;
    color: var(--ink);
    margin: 0;
  }
  .product {
    position: absolute;
    width: 206px;
    height: 206px;
    border-radius: 50%;
    background: var(--circle-face);
    box-shadow: -4px 6px 0 var(--accent-rose), 4px 8px 14px rgba(0,0,0,0.12);
    overflow: hidden;
  }
  .product__photo {
    position: absolute;
    inset: 22px;
    border-radius: 50%;
  }
  .product--tray { left: 29px; top: 415px; }
  .product--tray .product__photo { background: radial-gradient(circle, #c9a06a 0%, #a57b45 70%, #3b2f25 100%); inset: 30px 20px 40px; }
  .product--tote { left: 226px; top: 558px; }
  .product--tote .product__photo { background: linear-gradient(180deg, #e3cbc2, #c9aba0); border-radius: 6px; inset: 50px 52px 40px; }
  .product--earrings { left: 29px; top: 714px; }
  .product--earrings .product__photo { background: radial-gradient(circle, #e9cf7e 0%, #c9a74a 60%, #f9eff0 100%); inset: 50px 22px 60px; }
  .contact {
    position: absolute;
    right: 36px;
    top: 955px;
    text-align: right;
    font-family: "Quicksand", sans-serif;
    font-weight: 500;
    color: var(--ink);
    font-size: 23px;
    line-height: 1;
  }
  .contact__social {
    display: flex;
    align-items: center;
    justify-content: flex-end;
    gap: 10px;
    margin-top: 16px;
    padding-right: 40px;
  }
  .contact__dot {
    width: 28px;
    height: 28px;
    border: 3px solid var(--ink);
    border-radius: 50%;
    box-sizing: border-box;
  }
</style>
</head>
<body>
  <main class="banner">
    <svg class="banner__header" viewBox="0 0 460 300" aria-hidden="true">
      <path d="M0 0 H460 V245 Q230 345 0 245 Z" fill="var(--header-pink)"/>
      <path d="M0 245 Q230 345 460 245" fill="none" stroke="var(--accent-rose)" stroke-width="6"/>
    </svg>

    <div class="brand">
      <div class="brand__name">VERIKA</div>
      <div class="brand__sub">MODE</div>
    </div>

    <h1 class="tagline">Make your life beautiful</h1>

    <div class="product product--tray">
      <div class="product__photo" role="img" aria-label="Round leopard-print serving tray"></div>
    </div>
    <div class="product product--tote">
      <div class="product__photo" role="img" aria-label="Blush leather tote bag with teal snake detail"></div>
    </div>
    <div class="product product--earrings">
      <div class="product__photo" role="img" aria-label="Gold flower stud earrings with crystals"></div>
    </div>

    <div class="contact">
      <div class="contact__web">www.verikamode.com</div>
      <div class="contact__social">
        <span class="contact__dot"></span>
        <span class="contact__handle">verikamode</span>
      </div>
    </div>
  </main>
</body>
</html>
```